UI/UX Re-Do for TallyNest - a free to use project management platform for desktop and mobile.

UI/UX Re-Do for TallyNest
TallyNest is a free to use project management platform for desktop and mobile.
We are looking for help with our UI/UX re-design.
As of now the platform is totally functional.
The problem is around flow and look. We want TN to become something that any one can use to manage and even socialize any project. A project can be something work related like organizing a team around a software build, marketing campaign, shared client file space, etc... In fact, most of our current members are using TN for just such work projects.
We also see a project as planning a wedding, organizing a group trip, a simple to-do list, organizing a kids sports team, and so on...
To become a platform that people will use in their work and personal life we first need to become more intuitive and friendly - while maintaining advanced functionality for more advanced needs.
We need help to beautify, streamline, and simplify - while keeping all the functions.
The quickest way to understand TN, and our current issues is this short video:
https://vidhost.example/Qw8ZmT3pLsK
For sure see this link for the entire most recent description AND images:
https://tallynestapp.example/?p=KumrT4WdZeL
The best way to understand TN is to actually use it:
https://tallynestapp.example
Should you choose to take a run at improving TN here are the details:
Please focus your ideas for mobile, it's where we have the biggest issues.
Feel free to get outside the box.
Avoid swipe oriented designs.
Feel free to focus on ideas over polished outputs.
Use any tool you like, PS, hand drawing, written description if you think that works best.
(FYI - we use mostly use Vellum Slides docs internally)
Point is illustration of ideas over tool choice.
Feel free to:
Create something totally new
And/or riff on what we have now
And/or riff on the new design we are considering (see images below)
|||
If we go the direction of the images/designs below the idea is to give people options on how they see/experience TN.
Just below is what we are calling Base Mode. This is a more basic and simple flow. Probably a default to keep new users feeling comfortable at the start.
<img src="https://picbin.example/8hTzqWL.jpg" style="width: 100%;">
https://picbin.example/8hTzqWL.jpg
|||
We are calling this optional view Peak Mode. It is more advanced and can show all project, goal(renamed 'milestones') at the same time. This is more of a paint job on the current design.
<img src="https://picbin.example/vNmd2Rs.jpg" style="width: 100%;">
https://picbin.example/vNmd2Rs.jpg
|||
If you're submitting please let us know if you can also do the PS files for dev.
Not required, but once we nail down the concepts we want someone to hone in the PS files.
As an optional bonus we will also be giving credit to you/your company in TN.
Let us know if you do or don't want that.
We are excited to see your work!!
Target Market(s)
Anyone who needs to organize any project, big or small. The key is to make a super friendly user experience for new users while retaining advanced functions.
Industry/Entity Type
Management
Number of Pages Required
2 page
Look and feel

```html
<!DOCTYPE html>
<html lang="en">
<head>
<meta charset="utf-8">
<title>TallyNest mobile concepts</title>
<link href="https://fonts.googleapis.com/css2?family=Nunito+Sans:wght@400;600;700;800&display=swap" rel="stylesheet">
<style>
:root{
  --canvas:#a8a8a8;
  --bar-dark:#2d2d2d;
  --bar-sky:#3a85cb;
  --screen-bg:#f2f2f2;
  --project:#1f3d5b;
  --milestone:#2f79ba;
  --task:#7b7b7b;
  --orange:#f39a12;
  --stripe-yellow:#e6c21c;
  --stripe-green:#24a55b;
  --stripe-teal:#1d9e90;
  --stripe-purple:#8c3a8d;
  --ink:#333;
  --muted:#8a8a8a;
  --link:#2f79ba;
}
*{box-sizing:border-box;margin:0;padding:0}
html,body{width:1200px;height:945px;overflow:hidden;background:var(--canvas)}
body{font-family:"Nunito Sans",Arial,sans-serif}
.stage{position:absolute;left:0;top:0;width:1500px;height:1181px;transform:scale(.8);transform-origin:0 0}
.screen{position:absolute;width:272px;height:482px;background:var(--screen-bg);overflow:hidden}
.top{position:absolute;left:0;top:0;width:100%;height:46px;background:var(--bar-dark);color:#fff}
.top.sky{background:var(--bar-sky)}
.status{height:16px;display:flex;justify-content:space-between;align-items:center;padding:0 6px;font-size:6.5px;font-weight:600}
.battery{display:inline-block;width:12px;height:5px;background:#fff;border-radius:1px;margin-left:2px;vertical-align:middle}
.nav{position:relative;height:30px;display:flex;align-items:center;justify-content:center;font-size:11px;font-weight:700}
.nav .left{position:absolute;left:8px;top:8px;display:flex;align-items:center;gap:6px;font-size:8px}
.nav .right{position:absolute;right:8px;top:8px}
.ico{width:14px;height:14px;fill:none;stroke:currentColor;stroke-width:2;stroke-linecap:round;stroke-linejoin:round}
.avatar{width:20px;height:20px;border-radius:50%;background:linear-gradient(#a98d78,#5c4a3e);position:relative}
.avatar .badge{position:absolute;right:-5px;top:-3px;width:9px;height:9px;border-radius:50%;background:var(--orange);font-size:6px;text-align:center;line-height:9px;color:#fff}
.tabs{position:absolute;top:46px;left:0;width:100%;height:32px;background:#fff;display:flex;border-bottom:1px solid #dcdcdc}
.tab{flex:1;display:grid;place-items:center;color:#aaa;position:relative}
.tab.active{color:#7e8fa0;border-bottom:3px solid var(--milestone)}
.tab .ico{width:16px;height:16px;stroke-width:1.6}
.tab .dot{position:absolute;left:calc(50% + 5px);top:5px;width:9px;height:9px;border-radius:50%;background:var(--orange);color:#fff;font-size:6px;line-height:9px;text-align:center}
.row{position:absolute;height:30px;display:flex;color:#fff;font-size:10px;font-weight:700}
.row.project{background:var(--project)}
.row.milestone{background:var(--milestone)}
.row.task{background:var(--task)}
.row .label{flex:1;padding-left:9px;display:flex;align-items:center}
.row .cell{width:30px;display:grid;place-items:center;border-left:1px solid rgba(255,255,255,.15);font-size:9px;letter-spacing:-1px}
.row .cell .ico{width:12px;height:12px}
.s-yellow{border-left:3px solid var(--stripe-yellow)}
.s-green{border-left:3px solid var(--stripe-green)}
.s-teal{border-left:3px solid var(--stripe-teal)}
.s-purple{border-left:3px solid var(--stripe-purple)}
.fab{position:absolute;width:40px;height:40px;border-radius:50%;background:var(--orange);color:#fff;display:grid;place-items:center;box-shadow:0 2px 4px rgba(0,0,0,.25)}
.fab .ico{width:22px;height:22px;stroke-width:2.6}
.post{position:absolute;left:10px;width:252px;background:#fff;border:1px solid #e6e6e6;padding:6px 8px}
.post .head{display:flex;gap:6px;align-items:center}
.post .face{width:20px;height:20px;background:linear-gradient(#b59a84,#5b4a3f)}
.post .meta{font-size:6px;color:var(--muted);line-height:1.4}
.post .kebab{position:absolute;right:8px;top:8px;color:var(--milestone)}
.post p{font-size:8.5px;color:var(--ink);margin-top:9px;line-height:1.4}
.post a{color:var(--link);text-decoration:none}
.post .photo{margin-top:8px;height:108px;background:linear-gradient(135deg,#3b3b3b,#a9a9a9 45%,#d6d6d6 60%,#4a4a4a)}
.composer{position:absolute;left:0;top:450px;width:100%;height:32px;background:#f7f7f7;border-top:1px solid #ddd;display:flex;align-items:center;padding:0 6px 0 8px;gap:5px}
.composer .field{flex:1;height:24px;background:#fff;border:1px solid #ccc;font-size:8px;color:#aaa;padding:6px}
.composer .btn{width:24px;height:24px;border-radius:50%;background:var(--orange);display:grid;place-items:center;color:#fff}
.composer .btn .ico{width:13px;height:13px}
.sheet{position:absolute;left:0;top:282px;width:100%;height:200px;background:#fff;border-top:3px solid var(--orange)}
.form-row{position:absolute;left:0;width:100%;height:25px}
.form-row .lbl{position:absolute;left:0;width:48px;text-align:right;font-size:8.5px;color:#666;top:7px}
.form-row .input{position:absolute;left:53px;width:210px;height:25px;border:1px solid #ccc;font-size:8.5px;color:var(--ink);padding:6px 7px;display:flex;align-items:center;gap:4px}
.swatch{width:8px;height:8px;background:var(--milestone)}
.caret{position:absolute;right:8px;top:10px;width:0;height:0;border-left:4px solid transparent;border-right:4px solid transparent;border-top:4px solid #999}
.add-target{position:absolute;right:9px;top:148px;font-size:7.5px;font-weight:700;color:var(--orange)}
.actions{position:absolute;top:165px;left:53px;display:flex;gap:4px}
.actions span{width:86px;height:23px;border-radius:12px;display:grid;place-items:center;font-size:8.5px;font-weight:700}
.create{background:var(--orange);color:#fff}
.cancel{background:#ebebeb;color:#aaa}
.dim{position:absolute;inset:0;background:rgba(30,30,30,.62)}
.hot{position:absolute;left:202px;top:66px;width:30px;height:30px;background:var(--orange);color:#fff;display:grid;place-items:center;font-size:9px;letter-spacing:-1px}
.menu{position:absolute;left:134px;top:99px;width:96px;background:#fff;padding:3px 0}
.menu li{list-style:none;height:26px;display:flex;align-items:center;gap:6px;padding-left:7px;font-size:6.5px;font-weight:800;color:var(--orange)}
.menu li:first-child{color:var(--milestone)}
.menu .ico{width:10px;height:10px;color:#888}
</style>
</head>
<body>
<svg width="0" height="0" style="position:absolute">
  <defs>
    <symbol id="i-right" viewBox="0 0 24 24"><path d="M9 5l7 7-7 7"/></symbol>
    <symbol id="i-down" viewBox="0 0 24 24"><path d="M5 9l7 7 7-7"/></symbol>
    <symbol id="i-up" viewBox="0 0 24 24"><path d="M5 15l7-7 7 7"/></symbol>
    <symbol id="i-plus" viewBox="0 0 24 24"><path d="M12 4v16M4 12h16"/></symbol>
    <symbol id="i-search" viewBox="0 0 24 24"><circle cx="10" cy="10" r="6.5"/><path d="M15 15l5 5"/></symbol>
    <symbol id="i-menu" viewBox="0 0 24 24"><path d="M3 6h18M3 12h18M3 18h18"/></symbol>
    <symbol id="i-back" viewBox="0 0 24 24"><path d="M15 4l-8 8 8 8"/></symbol>
    <symbol id="i-list" viewBox="0 0 24 24"><path d="M8 6h13M8 12h13M8 18h13M3 6h1M3 12h1M3 18h1"/></symbol>
    <symbol id="i-chat" viewBox="0 0 24 24"><path d="M3 5h18v11H10l-5 4v-4H3z"/><path d="M8 10.5h.5M12 10.5h.5M16 10.5h.5"/></symbol>
    <symbol id="i-cal" viewBox="0 0 24 24"><rect x="3" y="5" width="18" height="16"/><path d="M3 9h18M8 3v4M16 3v4M9 15l2 2 4-4"/></symbol>
    <symbol id="i-people" viewBox="0 0 24 24"><circle cx="9" cy="8" r="3.5"/><circle cx="16" cy="9" r="3"/><path d="M2 20c0-4 3-6 7-6s7 2 7 6M15 14c4 0 7 2 7 5"/></symbol>
    <symbol id="i-pen" viewBox="0 0 24 24"><path d="M4 20l3-1L19 7l-2-2L5 17z"/></symbol>
    <symbol id="i-camera" viewBox="0 0 24 24"><path d="M3 8h4l2-3h6l2 3h4v12H3z"/><circle cx="12" cy="13" r="3.5"/></symbol>
    <symbol id="i-edit" viewBox="0 0 24 24"><path d="M4 20l3-1L19 7l-2-2L5 17z"/></symbol>
    <symbol id="i-copy" viewBox="0 0 24 24"><rect x="8" y="8" width="12" height="12"/><path d="M4 16V4h12"/></symbol>
    <symbol id="i-trash" viewBox="0 0 24 24"><path d="M4 6h16M9 6V3h6v3M6 6l1 15h10l1-15"/></symbol>
    <symbol id="i-addc" viewBox="0 0 24 24"><circle cx="12" cy="12" r="9" fill="currentColor"/><path d="M12 8v8M8 12h8" stroke="#fff"/></symbol>
    <symbol id="i-kebab" viewBox="0 0 24 24"><circle cx="12" cy="5" r="1.6" fill="currentColor"/><circle cx="12" cy="12" r="1.6" fill="currentColor"/><circle cx="12" cy="19" r="1.6" fill="currentColor"/></symbol>
  </defs>
</svg>

<main class="stage">

  <!-- Base Mode: project list -->
  <section class="screen" style="left:325px;top:72px">
    <header class="top">
      <div class="status"><span>●●●●● Carrier</span><span>5:30PM</span><span>100%<i class="battery"></i></span></div>
      <div class="nav"><span class="left"><svg class="ico"><use href="#i-menu"/></svg></span>MY PROJECTS<span class="right"><svg class="ico"><use href="#i-search"/></svg></span></div>
    </header>
    <div class="row project" style="left:9px;top:66px;width:254px"><span class="label">Project 1</span><span class="cell">•••</span><span class="cell"><svg class="ico"><use href="#i-right"/></svg></span></div>
    <div class="row project" style="left:9px;top:103px;width:254px"><span class="label">Project 2</span><span class="cell">•••</span><span class="cell"><svg class="ico"><use href="#i-right"/></svg></span></div>
    <div class="row project" style="left:9px;top:140px;width:254px"><span class="label">Project 3</span><span class="cell">•••</span><span class="cell"><svg class="ico"><use href="#i-right"/></svg></span></div>
    <div class="row project" style="left:9px;top:177px;width:254px"><span class="label">Project 4</span><span class="cell">•••</span><span class="cell"><svg class="ico"><use href="#i-right"/></svg></span></div>
    <div class="row project" style="left:9px;top:214px;width:254px"><span class="label">Project 5</span><span class="cell">•••</span><span class="cell"><svg class="ico"><use href="#i-plus"/></svg></span></div>
    <div class="row project" style="left:9px;top:251px;width:254px"><span class="label">Project 6</span><span class="cell">•••</span><span class="cell"><svg class="ico"><use href="#i-right"/></svg></span></div>
    <div class="row project" style="left:9px;top:288px;width:254px"><span class="label">Project 7</span><span class="cell">•••</span><span class="cell"><svg class="ico"><use href="#i-right"/></svg></span></div>
    <div class="row project" style="left:9px;top:325px;width:254px"><span class="label">Project 8</span><span class="cell">•••</span><span class="cell"><svg class="ico"><use href="#i-plus"/></svg></span></div>
    <div class="fab" style="left:223px;top:435px"><svg class="ico"><use href="#i-plus"/></svg></div>
  </section>

  <!-- Base Mode: project detail -->
  <section class="screen" style="left:614px;top:72px">
    <header class="top">
      <div class="status"><span>●●●●● Carrier</span><span>5:30PM</span><span>100%<i class="battery"></i></span></div>
      <div class="nav"><span class="left"><svg class="ico" style="width:10px"><use href="#i-back"/></svg>BACK</span>PROJECT 1<span class="right"><svg class="ico"><use href="#i-search"/></svg></span></div>
    </header>
    <nav class="tabs">
      <span class="tab active"><svg class="ico"><use href="#i-list"/></svg></span>
      <span class="tab"><svg class="ico"><use href="#i-chat"/></svg><i class="dot">1</i></span>
      <span class="tab"><svg class="ico"><use href="#i-cal"/></svg></span>
      <span class="tab"><svg class="ico"><use href="#i-people"/></svg></span>
      <span class="tab">•••</span>
    </nav>
    <div class="row milestone" style="left:9px;top:99px;width:254px"><span class="label">Milestone 1</span><span class="cell">•••</span><span class="cell"><svg class="ico"><use href="#i-right"/></svg></span></div>
    <div class="row milestone" style="left:9px;top:136px;width:254px"><span class="label">Milestone 2</span><span class="cell">•••</span><span class="cell"><svg class="ico"><use href="#i-right"/></svg></span></div>
    <div class="row milestone" style="left:9px;top:173px;width:254px"><span class="label">Milestone 3</span><span class="cell">•••</span><span class="cell"><svg class="ico"><use href="#i-right"/></svg></span></div>
    <div class="row milestone" style="left:9px;top:210px;width:254px"><span class="label">Milestone 4</span><span class="cell">•••</span><span class="cell"><svg class="ico"><use href="#i-plus"/></svg></span></div>
    <div class="row milestone" style="left:9px;top:247px;width:254px"><span class="label">Milestone 5</span><span class="cell">•••</span><span class="cell"><svg class="ico"><use href="#i-right"/></svg></span></div>
    <div class="row milestone" style="left:9px;top:284px;width:254px"><span class="label">Milestone 6</span><span class="cell">•••</span><span class="cell"><svg class="ico"><use href="#i-right"/></svg></span></div>
    <div class="row milestone" style="left:9px;top:321px;width:254px"><span class="label">Milestone 7</span><span class="cell">•••</span><span class="cell"><svg class="ico"><use href="#i-plus"/></svg></span></div>
    <div class="row milestone" style="left:9px;top:358px;width:254px"><span class="label">Milestone 8</span><span class="cell">•••</span><span class="cell"><svg class="ico"><use href="#i-right"/></svg></span></div>
    <div class="fab" style="left:223px;top:435px"><svg class="ico"><use href="#i-plus"/></svg></div>
  </section>

  <!-- Base Mode: milestone chat -->
  <section class="screen" style="left:903px;top:72px">
    <header class="top sky">
      <div class="status"><span>●●●●● Carrier</span><span>5:30PM</span><span>100%<i class="battery"></i></span></div>
      <div class="nav"><span class="left"><svg class="ico" style="width:10px"><use href="#i-back"/></svg>BACK</span>MILESTONE 2<span class="right"><svg class="ico"><use href="#i-search"/></svg></span></div>
    </header>
    <nav class="tabs">
      <span class="tab"><svg class="ico"><use href="#i-list"/></svg></span>
      <span class="tab active"><svg class="ico"><use href="#i-chat"/></svg><i class="dot">1</i></span>
      <span class="tab"><svg class="ico"><use href="#i-cal"/></svg></span>
      <span class="tab"><svg class="ico"><use href="#i-people"/></svg></span>
      <span class="tab">•••</span>
    </nav>
    <article class="post" style="top:100px;height:60px">
      <div class="head"><span class="face" role="img" aria-label="Profile photo of John Doe"></span><span class="meta">John Doe<br>9/15/2017 10:20am PDT</span></div>
      <svg class="ico kebab"><use href="#i-kebab"/></svg>
      <p>Harlow Brothers - movie</p>
    </article>
    <article class="post" style="top:168px;height:74px">
      <div class="head"><span class="face" role="img" aria-label="Profile photo of John Doe"></span><span class="meta">John Doe<br>9/19/2017 1:08pm PDT</span></div>
      <svg class="ico kebab"><use href="#i-kebab"/></svg>
      <p>help me video for small companies;<br><a>https://loafmotion.example/</a></p>
    </article>
    <article class="post" style="top:250px;height:160px">
      <div class="head"><span class="face" role="img" aria-label="Profile photo of John Doe"></span><span class="meta">John Doe<br>9/22/2017 4:05pm PDT</span></div>
      <svg class="ico kebab"><use href="#i-kebab"/></svg>
      <div class="photo" role="img" aria-label="Shared photo of a silver sports car"></div>
    </article>
    <div class="composer"><span class="field">Type here...</span><span class="btn"><svg class="ico"><use href="#i-chat"/></svg></span><span class="btn"><svg class="ico"><use href="#i-camera"/></svg></span></div>
  </section>

  <!-- Peak Mode: collapsed -->
  <section class="screen" style="left:36px;top:627px">
    <header class="top">
      <div class="status"><span>●●●●● Carrier</span><span>5:30PM</span><span>100%<i class="battery"></i></span></div>
      <div class="nav"><span class="left" style="top:5px"><svg class="ico"><use href="#i-menu"/></svg><span class="avatar" role="img" aria-label="User profile photo"><i class="badge">8</i></span></span>MY PROJECTS<span class="right"><svg class="ico"><use href="#i-search"/></svg></span></div>
    </header>
    <div class="row project s-yellow" style="left:9px;top:66px;width:254px"><span class="label">Project 1</span><span class="cell">•••</span><span class="cell"><svg class="ico"><use href="#i-down"/></svg></span></div>
    <div class="row project s-green" style="left:9px;top:103px;width:254px"><span class="label">Project 2</span><span class="cell">•••</span><span class="cell"><svg class="ico"><use href="#i-down"/></svg></span></div>
    <div class="row project s-teal" style="left:9px;top:140px;width:254px"><span class="label">Project 3</span><span class="cell">•••</span><span class="cell"><svg class="ico"><use href="#i-down"/></svg></span></div>
    <div class="row project s-purple" style="left:9px;top:177px;width:254px"><span class="label">Project 4</span><span class="cell">•••</span><span class="cell"><svg class="ico"><use href="#i-down"/></svg></span></div>
    <div class="row project s-yellow" style="left:9px;top:214px;width:254px"><span class="label">Project 5</span><span class="cell">•••</span><span class="cell"><svg class="ico"><use href="#i-plus"/></svg></span></div>
    <div class="row project s-green" style="left:9px;top:251px;width:254px"><span class="label">Project 6</span><span class="cell">•••</span><span class="cell"><svg class="ico"><use href="#i-down"/></svg></span></div>
    <div class="row project s-purple" style="left:9px;top:288px;width:254px"><span class="label">Project 7</span><span class="cell">•••</span><span class="cell"><svg class="ico"><use href="#i-down"/></svg></span></div>
    <div class="row project s-green" style="left:9px;top:325px;width:254px"><span class="label">Project 8</span><span class="cell">•••</span><span class="cell"><svg class="ico"><use href="#i-down"/></svg></span></div>
    <div class="fab" style="left:223px;top:433px"><svg class="ico"><use href="#i-plus"/></svg></div>
  </section>

  <!-- Peak Mode: expanded -->
  <section class="screen" style="left:325px;top:627px">
    <header class="top">
      <div class="status"><span>●●●●● Carrier</span><span>5:30PM</span><span>100%<i class="battery"></i></span></div>
      <div class="nav"><span class="left" style="top:5px"><svg class="ico"><use href="#i-menu"/></svg><span class="avatar" role="img" aria-label="User profile photo"><i class="badge">8</i></span></span>MY PROJECTS<span class="right"><svg class="ico"><use href="#i-search"/></svg></span></div>
    </header>
    <div class="row project s-yellow" style="left:9px;top:66px;width:254px"><span class="label">Project 1</span><span class="cell">•••</span><span class="cell"><svg class="ico"><use href="#i-up"/></svg></span></div>
    <div class="row milestone s-green" style="left:26px;top:101px;width:237px"><span class="label">Milestone 1</span><span class="cell">•••</span><span class="cell"><svg class="ico"><use href="#i-down"/></svg></span></div>
    <div class="row milestone s-green" style="left:26px;top:136px;width:237px"><span class="label">Milestone 2</span><span class="cell">•••</span><span class="cell"><svg class="ico"><use href="#i-plus"/></svg></span></div>
    <div class="row milestone s-purple" style="left:26px;top:171px;width:237px"><span class="label">Milestone 3</span><span class="cell">•••</span><span class="cell"><svg class="ico"><use href="#i-down"/></svg></span></div>
    <div class="row task s-purple" style="left:45px;top:205px;width:218px"><span class="label">Task 1</span><span class="cell">•••</span></div>
    <div class="row task s-purple" style="left:45px;top:240px;width:218px"><span class="label">Task 2</span><span class="cell">•••</span></div>
    <div class="row project s-green" style="left:9px;top:283px;width:254px"><span class="label">Project 2</span><span class="cell">•••</span><span class="cell"><svg class="ico"><use href="#i-down"/></svg></span></div>
    <div class="row project s-teal" style="left:9px;top:320px;width:254px"><span class="label">Project 3</span><span class="cell">•••</span><span class="cell"><svg class="ico"><use href="#i-down"/></svg></span></div>
    <div class="row project s-purple" style="left:9px;top:357px;width:254px"><span class="label">Project 4</span><span class="cell">•••</span><span class="cell"><svg class="ico"><use href="#i-down"/></svg></span></div>
    <div class="row project s-yellow" style="left:9px;top:394px;width:254px"><span class="label">Project 5</span><span class="cell">•••</span><span class="cell"><svg class="ico"><use href="#i-plus"/></svg></span></div>
    <div class="row project s-green" style="left:9px;top:431px;width:254px"><span class="label">Project 6</span><span class="cell">•••</span><span class="cell"><svg class="ico"><use href="#i-down"/></svg></span></div>
    <div class="row project s-purple" style="left:9px;top:468px;width:254px"><span class="label">Project 7</span><span class="cell">•••</span><span class="cell"><svg class="ico"><use href="#i-down"/></svg></span></div>
    <div class="fab" style="left:223px;top:433px"><svg class="ico"><use href="#i-plus"/></svg></div>
  </section>

  <!-- Peak Mode: create sheet -->
  <section class="screen" style="left:614px;top:627px">
    <header class="top">
      <div class="status"><span>●●●●● Carrier</span><span>5:30PM</span><span>100%<i class="battery"></i></span></div>
      <div class="nav"><span class="left" style="top:5px"><svg class="ico"><use href="#i-menu"/></svg><span class="avatar" role="img" aria-label="User profile photo"><i class="badge">8</i></span></span>MY PROJECTS<span class="right"><svg class="ico"><use href="#i-search"/></svg></span></div>
    </header>
    <div class="row project s-yellow" style="left:9px;top:66px;width:254px"><span class="label">Project 1</span><span class="cell">•••</span><span class="cell"><svg class="ico"><use href="#i-up"/></svg></span></div>
    <div class="row milestone s-green" style="left:26px;top:101px;width:237px"><span class="label">Milestone 1</span><span class="cell">•••</span><span class="cell"><svg class="ico"><use href="#i-down"/></svg></span></div>
    <div class="row milestone s-green" style="left:26px;top:136px;width:237px"><span class="label">Milestone 2</span><span class="cell">•••</span><span class="cell"><svg class="ico"><use href="#i-plus"/></svg></span></div>
    <div class="row milestone s-purple" style="left:26px;top:171px;width:237px"><span class="label">Milestone 3</span><span class="cell">•••</span><span class="cell"><svg class="ico"><use href="#i-down"/></svg></span></div>
    <div class="row task s-purple" style="left:45px;top:205px;width:218px"><span class="label">Task 1</span><span class="cell">•••</span></div>
    <div class="row task s-purple" style="left:45px;top:240px;width:218px"><span class="label">Task 2</span><span class="cell">•••</span></div>
    <div class="row project s-green" style="left:9px;top:279px;width:254px"><span class="label">Project 2</span><span class="cell">•••</span><span class="cell"><svg class="ico"><use href="#i-down"/></svg></span></div>
    <form class="sheet">
      <div class="form-row" style="top:25px"><span class="lbl">CRETAE:</span><span class="input"><i class="swatch"></i>New Milestone<i class="caret"></i></span></div>
      <div class="form-row" style="top:57px"><span class="lbl">NAME:</span><span class="input">Milestone 4</span></div>
      <div class="form-row" style="top:90px"><span class="lbl">ADD TO:</span><span class="input">Project 1<i class="caret"></i></span></div>
      <div class="form-row" style="top:115px"><span class="input">Project 3<i class="caret"></i></span></div>
      <span class="add-target">+ Add a target</span>
      <div class="actions"><span class="create">+ CREATE</span><span class="cancel">CANCEL</span></div>
    </form>
  </section>

  <!-- Peak Mode: project actions menu -->
  <section class="screen" style="left:903px;top:627px">
    <header class="top">
      <div class="status"><span>●●●●● Carrier</span><span>5:30PM</span><span>100%<i class="battery"></i></span></div>
      <div class="nav"><span class="left" style="top:5px"><svg class="ico"><use href="#i-menu"/></svg><span class="avatar" role="img" aria-label="User profile photo"><i class="badge">8</i></span></span>MY PROJECTS<span class="right"><svg class="ico"><use href="#i-search"/></svg></span></div>
    </header>
    <div class="row project s-yellow" style="left:9px;top:66px;width:254px"><span class="label">Project 1</span><span class="cell">•••</span><span class="cell"><svg class="ico"><use href="#i-up"/></svg></span></div>
    <div class="row milestone s-green" style="left:26px;top:101px;width:237px"><span class="label">Milestone 1</span><span class="cell">•••</span><span class="cell"><svg class="ico"><use href="#i-down"/></svg></span></div>
    <div class="row milestone s-green" style="left:26px;top:136px;width:237px"><span class="label">Milestone 2</span><span class="cell">•••</span><span class="cell"><svg class="ico"><use href="#i-plus"/></svg></span></div>
    <div class="row milestone s-purple" style="left:26px;top:171px;width:237px"><span class="label">Milestone 3</span><span class="cell">•••</span><span class="cell"><svg class="ico"><use href="#i-down"/></svg></span></div>
    <div class="row task s-purple" style="left:45px;top:205px;width:218px"><span class="label">Task 1</span><span class="cell">•••</span></div>
    <div class="row task s-purple" style="left:45px;top:240px;width:218px"><span class="label">Task 2</span><span class="cell">•••</span></div>
    <div class="row project s-green" style="left:9px;top:283px;width:254px"><span class="label">Project 2</span><span class="cell">•••</span><span class="cell"><svg class="ico"><use href="#i-down"/></svg></span></div>
    <div class="row project s-teal" style="left:9px;top:320px;width:254px"><span class="label">Project 3</span><span class="cell">•••</span><span class="cell"><svg class="ico"><use href="#i-down"/></svg></span></div>
    <div class="row project s-purple" style="left:9px;top:357px;width:254px"><span class="label">Project 4</span><span class="cell">•••</span><span class="cell"><svg class="ico"><use href="#i-down"/></svg></span></div>
    <div class="row project s-yellow" style="left:9px;top:394px;width:254px"><span class="label">Project 5</span><span class="cell">•••</span><span class="cell"><svg class="ico"><use href="#i-plus"/></svg></span></div>
    <div class="row project s-green" style="left:9px;top:431px;width:254px"><span class="label">Project 6</span><span class="cell">•••</span><span class="cell"><svg class="ico"><use href="#i-down"/></svg></span></div>
    <div class="row project s-purple" style="left:9px;top:468px;width:254px"><span class="label">Project 7</span><span class="cell">•••</span><span class="cell"><svg class="ico"><use href="#i-down"/></svg></span></div>
    <div class="fab" style="left:223px;top:433px"><svg class="ico"><use href="#i-plus"/></svg></div>
    <div class="dim"></div>
    <span class="hot">•••</span>
    <ul class="menu">
      <li><svg class="ico" style="color:var(--milestone)"><use href="#i-addc"/></svg>ADD MILESTONE</li>
      <li><svg class="ico"><use href="#i-edit"/></svg>EDIT PROJECT</li>
      <li><svg class="ico"><use href="#i-copy"/></svg>COPY PROJECT</li>
      <li><svg class="ico"><use href="#i-trash"/></svg>DELETE PROJECT</li>
    </ul>
  </section>

  <!-- Peak Mode: milestone chat -->
  <section class="screen" style="left:1192px;top:627px">
    <header class="top sky">
      <div class="status"><span>●●●●● Carrier</span><span>5:30PM</span><span>100%<i class="battery"></i></span></div>
      <div class="nav"><span class="left"><svg class="ico" style="width:10px"><use href="#i-back"/></svg>BACK</span>MILESTONE 1<span class="right"><svg class="ico"><use href="#i-search"/></svg></span></div>
    </header>
    <nav class="tabs">
      <span class="tab active"><svg class="ico"><use href="#i-chat"/></svg><i class="dot">1</i></span>
      <span class="tab"><svg class="ico"><use href="#i-cal"/></svg></span>
      <span class="tab"><svg class="ico"><use href="#i-pen"/></svg></span>
      <span class="tab"><svg class="ico"><use href="#i-people"/></svg></span>
      <span class="tab">•••</span>
    </nav>
    <article class="post" style="top:100px;height:60px">
      <div class="head"><span class="face" role="img" aria-label="Profile photo of John Doe"></span><span class="meta">John Doe<br>9/15/2017 10:20am PDT</span></div>
      <svg class="ico kebab"><use href="#i-kebab"/></svg>
      <p>Harlow Brothers - movie</p>
    </article>
    <article class="post" style="top:168px;height:74px">
      <div class="head"><span class="face" role="img" aria-label="Profile photo of John Doe"></span><span class="meta">John Doe<br>9/19/2017 1:08pm PDT</span></div>
      <svg class="ico kebab"><use href="#i-kebab"/></svg>
      <p>help me video for small companies;<br><a>https://loafmotion.example/</a></p>
    </article>
    <article class="post" style="top:250px;height:160px">
      <div class="head"><span class="face" role="img" aria-label="Profile photo of John Doe"></span><span class="meta">John Doe<br>9/22/2017 4:05pm PDT</span></div>
      <svg class="ico kebab"><use href="#i-kebab"/></svg>
      <div class="photo" role="img" aria-label="Shared photo of a silver sports car"></div>
    </article>
    <div class="composer"><span class="field">Type here...</span><span class="btn"><svg class="ico"><use href="#i-chat"/></svg></span><span class="btn"><svg class="ico"><use href="#i-camera"/></svg></span></div>
  </section>

</main>
</body>
</html>
```